Webesite for sales coach, keynote speaker, blog, author

Business is specifically targeted toward companies looking to optimise the performance of their sales teams with coaching, I would also like this to be a platform for an ongoing blog that will form the content for a book to be written next year. And lastly, as a destination for businesses to learn a little more about me to consider using me as a keynote speaker at their next business event. I need the format of the website to be easy editable by me going forward and ease in adding content and photographs where needed. Some examples of website styles i like include: http://www.brightmeadowplanner.example , http://tavomarine.example/ ,

Target Market(s)

Business Owners

Industry/Entity Type

Business Consultant

Coding

Coded - Design and coding required

Number of Pages Required

1 page

Font styles to use
Serif

Colors

Designer to choose colors to be used in the design.

Requirements
Must have
• Blog functionality (with ability for user to comment), ease of editing and adding new content, striking background photography that drives motivational thoughts (breath-taking landscape photography maybe?)

```html
<!DOCTYPE html>
<html lang="en">
<head>
<meta charset="utf-8">
<title>Corwenlake — Sales Coach, Keynote Speaker, Blog Author</title>
<link href="https://fonts.googleapis.com/css2?family=Alegreya+Sans:wght@400;500;700&family=Open+Sans:wght@400;600&display=swap" rel="stylesheet">
<style>
:root{
  --red:#e52d2d;
  --red-dark:#b8191c;
  --ink:#2b2b2b;
  --muted:#777;
  --hex-dark:#2f2f31;
  --line:#e4e4e4;
  --white:#fff;
  --soft:#f4f4f4;
}
*{box-sizing:border-box;margin:0;padding:0}
html,body{width:1200px;height:3772px;overflow:hidden}
body{position:relative;background:var(--white);color:var(--ink);font-family:"Open Sans",Arial,sans-serif}
.abs{position:absolute}

/* header */
.site-header{left:0;top:0;width:1200px;height:120px;background:var(--white)}
.brand{left:112px;top:34px;font-family:"Alegreya Sans",Georgia,serif;font-weight:500;font-size:30px;color:var(--ink)}
.main-nav{right:116px;top:52px;display:flex;gap:30px;font-size:13px;font-weight:600;letter-spacing:.5px}
.main-nav a{color:var(--ink);text-decoration:none}
.main-nav a.active{color:var(--red)}

/* hero */
.hero{left:0;top:120px;width:1200px;height:520px;background:linear-gradient(180deg,#3a4a5c 0%,#9c7a62 45%,#d98a4c 62%,#6a4f44 80%,#2d2622 100%)}
.hero-title{left:0;top:250px;width:1200px;text-align:center;color:var(--white);font-family:"Alegreya Sans",Georgia,serif;font-size:42px;line-height:50px;font-weight:500}
.hero-dots{left:0;top:474px;width:1200px;display:flex;justify-content:center;gap:10px}
.hero-dots span{width:12px;height:12px;border-radius:50%;background:rgba(255,255,255,.55)}
.hero-dots span.on{background:var(--white)}

/* bio intro */
.portrait{left:96px;top:530px;width:240px;height:230px;border:6px solid var(--white);background:linear-gradient(160deg,#b9c6cf,#7fa0b6);box-shadow:0 2px 8px rgba(0,0,0,.15)}
.bio-lead{left:384px;top:682px;width:720px;font-size:16px;line-height:26px;font-weight:600;color:var(--ink)}
.bio-text{left:384px;top:776px;width:720px;font-size:11px;line-height:19px;color:var(--muted)}
.btn-outline{left:384px;top:892px;width:100px;height:34px;border:1px solid #cfcfcf;font-size:10px;line-height:32px;text-align:center;color:var(--muted);letter-spacing:.5px}

/* section titles */
.section-title{left:0;width:1200px;text-align:center;font-family:"Alegreya Sans",Georgia,serif;font-size:32px;font-weight:500}
.swoosh{left:520px;width:160px;height:14px}

/* services */
.services{left:0;top:980px;width:1200px;height:760px}
.services-bg{left:0;top:0;width:1200px;height:760px}
.hex{width:240px;height:276px}
.hex-body{left:0;top:0;width:240px;height:276px;text-align:center;color:var(--white)}
.hex-title{position:absolute;left:0;top:112px;width:240px;font-family:"Alegreya Sans",Georgia,serif;font-size:17px;font-weight:500}
.hex-text{position:absolute;left:36px;top:142px;width:168px;font-size:9px;line-height:14px;color:rgba(255,255,255,.8)}
.hex-btn{position:absolute;left:111px;top:218px;width:18px;height:18px;border-radius:50%;background:var(--red)}
.hex.featured .hex-btn{background:var(--white)}

/* blog */
.blog{left:0;top:1720px;width:1200px;height:620px;background:linear-gradient(180deg,#fafafa 0%,#dcdcdc 55%,#cfcfcf 100%)}
.card{width:286px;height:356px;background:var(--white);box-shadow:0 2px 10px rgba(0,0,0,.12)}
.card-media{left:0;top:0;width:286px;height:184px}
.card-date{left:18px;top:200px;font-size:11px;font-weight:600}
.card-text{left:18px;top:224px;width:250px;font-size:10px;line-height:16px;color:var(--muted)}
.card-meta{left:18px;top:318px;font-size:9px;color:var(--muted)}
.card-meta b{color:var(--red);font-weight:600}
.pager{left:0;top:567px;width:1200px;display:flex;justify-content:center;gap:10px}
.pager span{width:24px;height:24px;border-radius:50%;background:#bdbdbd}
.pager span.on{background:var(--red)}

/* testimonials */
.testimonials{left:0;top:2300px;width:1200px;height:620px}
.avatar{left:300px;top:320px;width:164px;height:164px;border-radius:50%;border:6px solid var(--red);background:linear-gradient(160deg,#e8d7c8,#a9b9c9)}
.quote-name{left:500px;top:330px;font-family:"Alegreya Sans",Georgia,serif;font-size:18px;color:var(--white)}
.quote-text{left:500px;top:370px;width:420px;font-size:11px;line-height:19px;color:rgba(255,255,255,.85)}
.vdots{left:1100px;top:380px;display:flex;flex-direction:column;gap:12px}
.vdots span{width:10px;height:10px;border-radius:50%;background:rgba(255,255,255,.6)}
.vdots span.on{background:var(--red)}

/* newsletter */
.newsletter-sub{left:0;top:3058px;width:1200px;text-align:center;font-size:12px;color:#9a9a9a}
.signup{left:310px;top:3158px;width:590px;height:72px;display:flex}
.signup-input{width:432px;height:72px;border:1px solid var(--line);font-size:11px;line-height:70px;padding-left:26px;color:#aaa}
.signup-btn{width:158px;height:72px;background:var(--red);color:var(--white);font-size:12px;font-weight:600;line-height:72px;text-align:center}

/* photo feed */
.feed{left:0;top:3302px;width:1200px;height:220px;display:flex}
.feed div{width:200px;height:220px}
.feed-label{left:0;top:3430px;width:200px;text-align:center;color:var(--white);font-family:"Alegreya Sans",Georgia,serif;font-size:18px;font-weight:500}

/* footer */
.footer-brand{left:0;top:3580px;width:1200px;text-align:center;font-family:"Alegreya Sans",Georgia,serif;font-weight:500;font-size:30px}
.footer-social{left:0;top:3668px;width:1200px;display:flex;justify-content:center;gap:12px}
.footer-social span{width:26px;height:26px;border-radius:50%;border:1px solid #bbb}
.copyright{left:0;top:3726px;width:1200px;text-align:center;font-size:10px;color:var(--muted)}
</style>
</head>
<body>

<header class="site-header abs">
  <div class="brand abs">Corwenlake.example</div>
  <nav class="main-nav abs"><a class="active" href="#">HOME</a><a href="#">BIO</a><a href="#">SERVICES</a><a href="#">MEDIA</a><a href="#">CONTACT</a></nav>
</header>

<section class="hero abs" role="img" aria-label="Landscape photograph: a hiker standing on a mountain ridge at sunset">
  <h1 class="hero-title abs">Phasellus Nisl Est<br>Condimentum Vitae Faucibus</h1>
  <div class="hero-dots abs"><span class="on"></span><span></span><span></span></div>
</section>

<div class="portrait abs" role="img" aria-label="Portrait photograph of the coach"></div>
<p class="bio-lead abs">Pellentesque blandit lacus eget nunc faucibus, et tincidunt ante viverra. Phasellus consequat sagittis nisi suscipit feugiat. Cras eget leo sed nunc hem diamb ultricies eu et nisl. Fusce eget neque elit.</p>
<p class="bio-text abs">Vestibulum condimentum nisi a mauris cursus, nec pretium justo luctus. Curabitur varius felis in lorem tempor, sit amet posuere dolor facilisis. Donec gravida magna vitae sapien pulvinar, at interdum nulla placerat. Aliquam erat volutpat. Morbi tristique quam sed velit dictum, non fermentum augue hendrerit. Integer faucibus orci eu tortor blandit, id porta leo varius. Sed consequat urna vel turpis aliquet, quis efficitur massa tempus. Nam luctus arcu at mi ultrices aliquet.</p>
<div class="btn-outline abs">READ MORE</div>

<section class="services abs">
  <svg class="services-bg abs" viewBox="0 0 1200 760" role="img" aria-label="Black and white photograph of a hiker on a mountain summit">
    <defs><linearGradient id="gSrv" x1="0" y1="0" x2="0" y2="1"><stop offset="0" stop-color="#cfcfcf"/><stop offset=".5" stop-color="#9a9a9a"/><stop offset="1" stop-color="#6f6f6f"/></linearGradient></defs>
    <polygon points="0,0 1200,60 1200,760 0,700" fill="url(#gSrv)"/>
  </svg>
  <h2 class="section-title abs" style="top:108px;color:var(--ink)">What We do?</h2>
  <svg class="swoosh abs" style="top:152px" viewBox="0 0 160 14"><path d="M4 10 Q80 0 156 8" stroke="#e52d2d" stroke-width="3" fill="none" stroke-linecap="round"/></svg>

  <div class="hex abs" style="left:240px;top:200px">
    <svg class="abs" width="240" height="276" viewBox="0 0 240 276"><polygon points="120,0 240,69 240,207 120,276 0,207 0,69" fill="#2f2f31"/>
      <polyline points="96,92 108,76 118,84 134,66 144,72" stroke="#fff" stroke-width="2" fill="none"/><line x1="94" y1="94" x2="146" y2="94" stroke="#fff" stroke-width="2"/></svg>
    <div class="hex-body abs"><div class="hex-title">Sales Coach</div><div class="hex-text">Sed ut perspiciatis unde omnis iste natus error sit voluptatem accusantium doloremque laudantium</div><div class="hex-btn"></div></div>
  </div>
  <div class="hex featured abs" style="left:480px;top:200px">
    <svg class="abs" width="240" height="276" viewBox="0 0 240 276"><polygon points="120,0 240,69 240,207 120,276 0,207 0,69" fill="#e52d2d"/>
      <path d="M100 74 L126 64 L126 92 L100 82 Z M92 74 H100 V82 H92 Z" stroke="#fff" stroke-width="2" fill="none"/><line x1="132" y1="78" x2="142" y2="78" stroke="#fff" stroke-width="2"/></svg>
    <div class="hex-body abs"><div class="hex-title">Keynote Speaker</div><div class="hex-text">Sed ut perspiciatis unde omnis iste natus error sit voluptatem accusantium doloremque laudantium</div><div class="hex-btn"></div></div>
  </div>
  <div class="hex abs" style="left:720px;top:200px">
    <svg class="abs" width="240" height="276" viewBox="0 0 240 276"><polygon points="120,0 240,69 240,207 120,276 0,207 0,69" fill="#2f2f31"/>
      <path d="M104 96 L140 62 Q136 84 112 92 Z" stroke="#fff" stroke-width="2" fill="none"/></svg>
    <div class="hex-body abs"><div class="hex-title">Blog Author</div><div class="hex-text">Sed ut perspiciatis unde omnis iste natus error sit voluptatem accusantium doloremque laudantium</div><div class="hex-btn"></div></div>
  </div>
</section>

<section class="blog abs" role="img" aria-label="Faded landscape photograph behind the blog section">
  <h2 class="section-title abs" style="top:44px">Blog</h2>
  <svg class="swoosh abs" style="top:88px" viewBox="0 0 160 14"><path d="M4 10 Q80 0 156 8" stroke="#e52d2d" stroke-width="3" fill="none" stroke-linecap="round"/></svg>

  <article class="card abs" style="left:148px;top:160px">
    <div class="card-media abs" role="img" aria-label="Photograph of a laptop on a desk" style="background:linear-gradient(150deg,#4a4a4c,#2a2a2c)"></div>
    <div class="card-date abs">July 25th 2017</div>
    <p class="card-text abs">Sed ut perspiciatis unde omnis iste natus error sit voluptatem accusantium doloremque laudantium</p>
    <div class="card-meta abs">Posted by <b>Administrator</b></div>
  </article>
  <article class="card abs" style="left:457px;top:160px">
    <div class="card-media abs" role="img" aria-label="Photograph of a business meeting" style="background:linear-gradient(150deg,#9fb1bf,#5f7384)"></div>
    <div class="card-date abs">July 25th 2017</div>
    <p class="card-text abs">Sed ut perspiciatis unde omnis iste natus error sit voluptatem accusantium doloremque laudantium</p>
    <div class="card-meta abs">Posted by <b>Administrator</b></div>
  </article>
  <article class="card abs" style="left:766px;top:160px">
    <div class="card-media abs" role="img" aria-label="Photograph of people working in an office" style="background:linear-gradient(150deg,#c7b9a6,#7a6b5c)"></div>
    <div class="card-date abs">July 25th 2017</div>
    <p class="card-text abs">Sed ut perspiciatis unde omnis iste natus error sit voluptatem accusantium doloremque laudantium</p>
    <div class="card-meta abs">Posted by <b>Administrator</b></div>
  </article>
  <div class="pager abs"><span></span><span class="on"></span></div>
</section>

<section class="testimonials abs">
  <svg class="abs" style="left:0;top:0" width="1200" height="620" viewBox="0 0 1200 620" role="img" aria-label="Dark photograph of a person standing on a cliff overlooking mountains">
    <defs><linearGradient id="gTst" x1="0" y1="0" x2="0" y2="1"><stop offset="0" stop-color="#6a6a6a"/><stop offset=".6" stop-color="#3f3f3f"/><stop offset="1" stop-color="#262626"/></linearGradient></defs>
    <polygon points="0,60 1200,0 1200,600 0,520" fill="url(#gTst)"/>
  </svg>
  <h2 class="section-title abs" style="top:170px;color:var(--white)">Testimonials</h2>
  <svg class="swoosh abs" style="top:214px" viewBox="0 0 160 14"><path d="M4 10 Q80 0 156 8" stroke="#e52d2d" stroke-width="3" fill="none" stroke-linecap="round"/></svg>
  <div class="avatar abs" role="img" aria-label="Portrait photograph of the client giving the testimonial"></div>
  <div class="quote-name abs">Arlen Whitby</div>
  <p class="quote-text abs">Sed ut perspiciatis unde omnis iste natus error sit voluptatem accusantium doloremque laudantium, totam rem aperiam eaque ipsa quae ab illo inventore veritatis et quasi architecto beatae vitae dicta sunt explicabo. Nemo enim ipsam voluptatem.</p>
  <div class="vdots abs"><span class="on"></span><span></span><span></span></div>
</section>

<h2 class="section-title abs" style="top:2996px">Newsletter Sign Up</h2>
<p class="newsletter-sub abs">Get the latest coaching insights and new blog posts sent to your inbox.</p>
<div class="signup abs"><div class="signup-input">Enter your e-mail address</div><div class="signup-btn">Subscribe Now</div></div>

<div class="feed abs">
  <div role="img" aria-label="Feed photo of a business team" style="background:linear-gradient(160deg,#8a1a1c,#3a1012)"></div>
  <div role="img" aria-label="Feed photo of a handshake" style="background:linear-gradient(160deg,#d6d6d6,#8c8c8c)"></div>
  <div role="img" aria-label="Feed photo of a speaker on stage" style="background:linear-gradient(160deg,#5a5a5a,#2e2e2e)"></div>
  <div role="img" aria-label="Feed photo of a desk with notebook" style="background:linear-gradient(160deg,#cbbba6,#8a7865)"></div>
  <div role="img" aria-label="Feed photo of a team at work" style="background:linear-gradient(160deg,#b7b7b7,#6a6a6a)"></div>
  <div role="img" aria-label="Feed photo of a workspace" style="background:linear-gradient(160deg,#e6e6e6,#a8a8a8)"></div>
</div>
<div class="feed-label abs">Photo Feed</div>

<footer>
  <div class="footer-brand abs">Corwenlake.example</div>
  <div class="footer-social abs"><span></span><span></span><span></span><span></span><span></span><span></span></div>
  <p class="copyright abs">© 2017 Company Name | All Rights Reserved</p>
</footer>

</body>
</html>
```